VELDOR SYSTEMS Swift Strand Service - one page design to attract buyers to buy fiber

Veldor Systems builds fiber optic cables. This landing page is designed to attract new clients who need fiber optic cables built and shipped very quickly. The overall design should show images that promote "fast" as well as "quality." These are data center fiber cables. You can use your imagination on this. We want someone to look at the page and think, "these guys can get my cable built very fast and I'm comfortable with their quality." Here is a link of examples of the fiber cables:
https://veldorsys.example/jumpers-patch-cords-fiber-optic-cable-assemblies/

Target Market(s)

Men 30-60

Colors

Designer to choose colors to be used in the design.

Requirements
Must have
• At the top of the page, it should read "Veldor Systems Swift Strand Service"
• There should also be a prominent button somewhere on the page that says "Swift Strand" which will lead to an email address.
• The content on the page is the following:
• Go ahead, press the button and experience Veldor's Swift Strand Service. We know you can't wait for your cables so we're prepared to help you. Our facility is located in Rivermont, Oregon and specialize in TAA compliant, certified cables assemblies. With our state of the art fiber equipment and dedicated engineers, we can build your custom cable so that you don't miss that deadline!
• Here are just a few of the types of cables we build:
• Connector Configuration: LC, SC, ST, FC, MTRJ, MTP, APC, UPC and more. Jacket Type: Indoor/Outdoor, Armored, Aerial, Tactical, Zip Cord, Tight Buffered and more.
• Jacket Rating: Plenum & Riser Rated (OFNR / OFNP)
• Modality: Multimode OM1, OM2, OM3, OM4 & Singlemode OS2
• Fiber Count: 1, 2, 4, 6, 8, 12, 24, 48 , 96, 144 Fiber Strands
• sales@veldorsys.example
• phone (555) 318-2946
• Please also include FB, Twitter and Link'd in icons at the bottom
Nice to have
• Would like to see anything that promotes fast. Something unique (not a car or a plane) I would like something different. You can use more than one image. Use your imagination on this. Be creative.
• Please use Veldor Company logo as well as the TAA compliant and made in usa logo. The Veldor logo is more important than those two logos.
Should not have
• no cartoons or anything whimsical

```html
<!DOCTYPE html>
<html lang="en">
<head>
<meta charset="utf-8">
<title>Veldor Systems — Swift Strand Service</title>
<link rel="stylesheet" href="https://fonts.googleapis.com/css2?family=Source+Sans+3:wght@400;600;700&family=Montserrat:wght@500;600;700&family=Roboto:wght@400;500&display=swap">
<style>
:root{
  --blue:#1e6fc1;
  --yellow:#f7b500;
  --ink:#111111;
  --grey-text:#6f7480;
  --page:#f3f4f6;
  --topbar:#f2f2f2;
  --footer:#262d3d;
  --footer-bar:#4b576c;
  --footer-text:#d9dce2;
  --cream:#fdf5e2;
}
*{box-sizing:border-box;margin:0;padding:0}
html,body{width:1200px;height:2700px;overflow:hidden;background:#fff}
body{position:relative;font-family:"Roboto",Arial,sans-serif;color:var(--ink)}
.abs{position:absolute}

/* top bar */
.topbar{left:95px;top:91px;width:1010px;height:32px;background:var(--topbar);font-size:10px;color:var(--grey-text)}
.topbar-question{position:absolute;left:164px;top:10px}
.topbar-contacts{position:absolute;right:164px;top:10px;display:flex;gap:22px;white-space:nowrap}
.topbar-contacts span{display:flex;align-items:center;gap:4px}
.header{left:95px;top:123px;width:1010px;height:76px;background:#fff}
.brand{left:139px;top:22px;display:flex;align-items:center;gap:8px;font-family:"Source Sans 3",sans-serif;font-weight:700;font-size:26px;color:#1b1b1b;letter-spacing:1px;white-space:nowrap}
.brand-mark{width:14px;height:14px;background:var(--blue)}
.nav-list{position:absolute;left:562px;top:28px;display:flex;align-items:center;gap:21px;font-size:10.5px;color:#222;white-space:nowrap}
.nav-list .active{color:var(--blue)}

/* hero */
.hero{left:95px;top:199px;width:1010px;height:530px;background:linear-gradient(180deg,#1d2f57 0%,#27406e 45%,#4a4a5a 72%,#7a5a55 100%)}
.hero-title{left:258px;top:322px;font-family:"Source Sans 3",sans-serif;font-weight:700;font-size:47px;line-height:48px;color:#fff;text-transform:uppercase;letter-spacing:-.3px;white-space:nowrap}
.hero-lines{left:251px;top:484px;font-family:"Source Sans 3",sans-serif;font-weight:700;font-size:13.5px;color:#fff;white-space:nowrap}
.hero-lines span{display:table;background:#000;padding:1px 9px;margin-bottom:3px;line-height:20px}
.btn-explore{left:256px;top:578px;width:107px;height:36px;background:var(--blue);color:#fff;font-family:"Source Sans 3",sans-serif;font-weight:700;font-size:15px;display:flex;align-items:center;justify-content:center;box-shadow:3px 3px 5px rgba(0,0,0,.45)}

/* band */
.band{left:95px;top:729px;width:1010px;height:62px;background:var(--yellow)}
.band-text{left:204px;top:19px;font-family:"Source Sans 3",sans-serif;font-size:19px;color:#fff;white-space:nowrap}
.band-text a{color:#111;text-decoration:underline}
.btn-swift{left:796px;top:17px;height:29px;padding:0 4px;background:#fff;color:var(--yellow);font-family:"Source Sans 3",sans-serif;font-weight:700;font-size:19px;display:flex;align-items:center;text-decoration:none;white-space:nowrap}

/* main grey area */
.main{left:95px;top:791px;width:1010px;height:1511px;background:var(--page)}
.about-title{left:230px;top:880px;font-family:"Montserrat",sans-serif;font-weight:700;font-size:30px}
.about-text{left:228px;top:932px;font-size:13.5px;line-height:16.5px;text-transform:uppercase;color:#222;white-space:nowrap}
.btn-read{left:228px;top:1022px;width:97px;height:36px;background:var(--blue);color:#fff;font-family:"Source Sans 3",sans-serif;font-weight:700;font-size:15px;display:flex;align-items:center;justify-content:center;box-shadow:3px 3px 5px rgba(0,0,0,.4)}
.video-accent{left:817px;top:864px;width:187px;height:126px;background:var(--blue)}
.video{left:639px;top:877px;width:346px;height:212px;background:#000}
.video-tag{right:6px;bottom:6px;width:90px;height:7px;background:var(--blue);color:#fff;font-size:5px;letter-spacing:1px;text-align:center;line-height:7px;font-weight:700}

.section-title{left:0;width:1200px;text-align:center;font-family:"Montserrat",sans-serif;font-weight:700;font-size:30px}
.section-desc{left:0;width:1200px;text-align:center;font-size:8.5px;line-height:14.5px;color:var(--grey-text)}
.filters{left:0;width:1200px;top:1262px;display:flex;justify-content:center;gap:11px;font-size:8.5px;color:#222}
.filters .on{color:var(--yellow);text-decoration:underline}

.tile{position:absolute}
.tile-hover{left:436px;top:1297px;width:327px;height:138px;background:var(--yellow)}
.tile-caption{left:436px;top:1435px;width:327px;height:59px;background:var(--cream)}
.tile-caption h3{position:absolute;left:18px;top:16px;font-family:"Source Sans 3",sans-serif;font-weight:400;font-size:16px;color:#444}
.tile-caption .rule{position:absolute;left:18px;top:42px;width:32px;height:1px;background:#777}
.tile-btn{position:absolute;top:23px;width:23px;height:21px;background:var(--yellow);display:flex;align-items:center;justify-content:center}

.card-img{top:1930px;width:216px;height:141px}
.card-title{top:2090px;width:230px;font-family:"Montserrat",sans-serif;font-weight:600;font-size:13px;line-height:18px;color:#333;text-transform:uppercase}
.card-date{top:2131px;font-size:6.5px;color:#777;display:flex;align-items:center;gap:4px}
.card-text{top:2151px;width:220px;font-size:8px;line-height:14px;color:var(--grey-text)}
.card-more{top:2205px;font-size:8px;color:#666}
.card-more.on{color:var(--yellow);text-decoration:underline}

/* footer */
.footer{left:93px;top:2302px;width:1010px;height:269px;background:var(--footer)}
.footer-bar{left:93px;top:2571px;width:1010px;height:34px;background:var(--footer-bar)}
.f-head{top:2349px;font-size:8px;color:var(--footer-text)}
.f-list{list-style:none;font-size:7px;color:#fff;line-height:26px}
.f-list li::before{content:"» ";}
.f-news{display:flex;gap:8px;font-size:7px;color:#fff;line-height:12px}
.f-news .thumb{width:38px;height:38px;flex:none}
.f-news small{display:block;font-size:5px}
.f-contact{font-size:7px;color:#fff;line-height:13px;display:flex;gap:8px}
.f-social{display:flex;gap:12px}
.f-social i{display:block;width:10px;height:10px;background:#fff;border-radius:2px}
.f-input{left:775px;top:2415px;width:120px;height:21px;background:#fff;font-size:6px;color:#999;padding:7px 11px}
.f-done{left:895px;top:2415px;width:42px;height:21px;background:var(--yellow);color:#fff;font-size:6px;font-weight:700;text-align:center;line-height:21px}
.badge{top:2496px;height:45px;background:#fff}
.bar-text{top:2584px;font-size:7px;color:#fff}
</style>
</head>
<body>

<div class="abs topbar">
  <span class="topbar-question">Have any question?</span>
  <div class="topbar-contacts">
    <span>
      <svg width="11" height="8" viewBox="0 0 11 8"><rect x=".5" y=".5" width="10" height="7" fill="none" stroke="#888"/><path d="M.5 .5l5 4 5-4" fill="none" stroke="#888"/></svg>
      sales@veldorsys.example</span>
    <span>
      <svg width="9" height="9" viewBox="0 0 9 9"><path d="M2 1l1.5 2-1 1c.6 1.2 1.3 1.9 2.5 2.5l1-1L8 7 7 8.5C4 8 1 5 .5 2z" fill="none" stroke="#888" stroke-width=".8"/></svg>
      (555) 318-2946</span>
  </div>
</div>

<header class="abs header">
  <div class="abs brand"><span class="brand-mark"></span>VELDOR SYSTEMS</div>
  <nav class="nav-list">
    <span class="active">About</span>
    <span>Products</span>
    <span>Services</span>
    <span>Ressources</span>
    <span>Contact</span>
    <svg width="9" height="9" viewBox="0 0 9 9" style="margin-left:-13px"><circle cx="3.5" cy="3.5" r="2.6" fill="none" stroke="#222" stroke-width="1.3"/><path d="M5.5 5.5L8.5 8.5" stroke="#222" stroke-width="1.5"/></svg>
  </nav>
</header>

<section class="abs hero" role="img" aria-label="Night city skyline with long-exposure light trails streaking along a highway"></section>
<h1 class="abs hero-title">Go ahead, press the button<br>and experience Veldor's<br>Swift Strand Service</h1>
<div class="abs hero-lines">
  <span>We know you can't wait for your cables so we're prepared to help you</span>
  <span>Our facility is located in Rivermont, Oregon and specialize in TAA</span>
  <span>compliant, certified cables assemblies</span>
</div>
<div class="abs btn-explore">Explore Now</div>

<div class="abs band">
  <p class="abs band-text">Consulting And Estimate For Your Project, <a>Contact Us Today</a></p>
  <a class="abs btn-swift" href="mailto:sales@veldorsys.example">Swift Strand</a>
</div>

<main class="abs main"></main>

<h2 class="abs about-title">ABOUT US</h2>
<p class="abs about-text">Lorem ipsum dolor sit amet, consectetur adipiscing elit,<br>sed do eiusmod tempor incididunt<br>ut labore et dolore magna aliqua.<br>Enim nec dui nunc mattis enim.</p>
<div class="abs btn-read">READ MORE</div>
<div class="abs video-accent"></div>
<div class="abs video" role="img" aria-label="Company story video">
  <svg class="abs" style="left:158px;top:88px" width="34" height="38" viewBox="0 0 34 38"><path d="M4 4q0-3 3-1.5l23 14q3 2.5 0 5l-23 14Q4 37 4 34z" fill="none" stroke="#fff" stroke-width="2.4" stroke-linejoin="round"/></svg>
  <div class="abs video-tag">OUR STORY</div>
</div>

<h2 class="abs section-title" style="top:1148px">OUR PRODUCTS</h2>
<p class="abs section-desc" style="top:1199px">Lorem ipsum dolor sit amet, sed dicunt oporteat cu, laboramus definiebas cum et. Duo id omnis<br>persequeris neglegentur, facete commodo ea usu, possit lucilius sed ei. Esse efficiendi scripserit eos ex.<br>Sea utamur iisque salutatus id.Mel autem animal.</p>
<nav class="abs filters"><span>All</span><span class="on">Green Building</span><span>Healthcare</span><span>Interior Design</span><span>Office</span></nav>

<div class="tile" style="left:95px;top:1293px;width:336px;height:204px;background:#fcc1a6"></div>
<div class="tile" style="left:432px;top:1293px;width:335px;height:204px;background:#fff"></div>
<div class="tile tile-hover"></div>
<div class="tile tile-caption">
  <h3>Fiber Enclosures and Parts</h3><span class="rule"></span>
  <span class="tile-btn" style="left:258px"><svg width="9" height="9"><path d="M4.5 1v7M1 4.5h7" stroke="#fff" stroke-width="1.2"/></svg></span>
  <span class="tile-btn" style="left:288px"><svg width="9" height="9"><path d="M3 6l3-3M2.5 4.5l-1 1a1.4 1.4 0 002 2l1-1M6.5 4.5l1-1a1.4 1.4 0 00-2-2l-1 1" fill="none" stroke="#fff" stroke-width="1"/></svg></span>
</div>
<div class="tile" style="left:768px;top:1293px;width:336px;height:204px;background:var(--blue)"></div>
<div class="tile" style="left:95px;top:1497px;width:336px;height:204px;background:#fdf8a8"></div>
<div class="tile" style="left:432px;top:1497px;width:335px;height:204px;background:#a8fedd"></div>
<div class="tile" style="left:768px;top:1497px;width:336px;height:204px;background:#f6f068"></div>

<h2 class="abs section-title" style="top:1777px;font-weight:600;color:#2e3441">OUR FEATURED NEWS</h2>
<p class="abs section-desc" style="top:1828px">Lorem ipsum dolor sit amet, sed dicunt oporteat cu, laboramus definiebas cum et. Duo id omnis<br>persequeris neglegentur, facete commodo ea usu, possit lucilius sed ei. Esse efficiendi scripserit eos ex.<br>Sea utamur iisque salutatus id.Mel autem animal.</p>

<article>
  <div class="abs card-img" style="left:260px;background:#a5a5fc"></div>
  <h3 class="abs card-title" style="left:260px">Construction Forklift<br>Buyers Guide</h3>
  <div class="abs card-date" style="left:260px"><svg width="7" height="7"><rect x=".5" y="1" width="6" height="5.5" fill="none" stroke="#777" stroke-width=".8"/></svg>12 DECEMBER 2018</div>
  <p class="abs card-text" style="left:260px">Lorem ipsum dolor sit amet, sed dicunt oporteat cuum Tuo iomnis persequeris neglegentur, facete commodo ea use possit lucilius.</p>
  <span class="abs card-more on" style="left:260px">READ MORE</span>
</article>
<article>
  <div class="abs card-img" style="left:494px;background:var(--yellow)"></div>
  <h3 class="abs card-title" style="left:494px">How to plan for your<br>dream house?</h3>
  <div class="abs card-date" style="left:494px"><svg width="7" height="7"><rect x=".5" y="1" width="6" height="5.5" fill="none" stroke="#777" stroke-width=".8"/></svg>12 DECEMBER 2018</div>
  <p class="abs card-text" style="left:494px">Lorem ipsum dolor sit amet, sed dicunt oporteat cuum Tuo iomnis persequeris neglegentur, facete commodo ea use possit lucilius.</p>
  <span class="abs card-more" style="left:494px">READ MORE</span>
</article>
<article>
  <div class="abs card-img" style="left:727px;background:#cda5fc"></div>
  <h3 class="abs card-title" style="left:727px">Builder of human<br>happiness for all time</h3>
  <div class="abs card-date" style="left:727px"><svg width="7" height="7"><rect x=".5" y="1" width="6" height="5.5" fill="none" stroke="#777" stroke-width=".8"/></svg>12 DECEMBER 2018</div>
  <p class="abs card-text" style="left:727px">Lorem ipsum dolor sit amet, sed dicunt oporteat cuum Tuo iomnis persequeris neglegentur, facete commodo ea use possit lucilius.</p>
  <span class="abs card-more" style="left:727px">READ MORE</span>
</article>

<footer class="abs footer"></footer>
<span class="abs f-head" style="left:238px">Recent Posts</span>
<ul class="abs f-list" style="left:238px;top:2371px">
  <li>How you can impact your customers.</li>
  <li>Construction is all about quality.</li>
  <li>Is your website user friendly?</li>
  <li>HUGE offers weekly updates &amp; more.</li>
  <li>Your customers should love your web.</li>
</ul>

<span class="abs f-head" style="left:418px">Recent News</span>
<div class="abs f-news" style="left:418px;top:2380px"><span class="thumb" style="background:#fd7d7d"></span><div>A Clean Website Gives More<br>Experience To The Visitors<small>Dec 12 - 2018</small></div></div>
<div class="abs f-news" style="left:418px;top:2433px"><span class="thumb" style="background:#72fdf0"></span><div>A Clean Website Gives More<br>Experience To The Visitors<small>Dec 12 - 2018</small></div></div>

<span class="abs f-head" style="left:597px">Contact Info</span>
<div class="abs f-contact" style="left:597px;top:2381px"><svg width="9" height="7"><rect x=".5" y=".5" width="8" height="6" fill="none" stroke="#fff"/><path d="M.5 .5l4 3 4-3" fill="none" stroke="#fff"/></svg>hello@northwave.example</div>
<div class="abs f-contact" style="left:597px;top:2407px"><svg width="8" height="8"><path d="M2 1l1.3 1.8-.9.9c.5 1 1.2 1.7 2.2 2.2l.9-.9L7 6.3 6 7.5C3.5 7 1 4.5.5 2z" fill="#fff"/></svg><span>P: 5550 148 2207<br>F: 5550 148 2208</span></div>
<div class="abs f-contact" style="left:597px;top:2446px"><svg width="7" height="9"><path d="M3.5 9S.5 5.5.5 3.5a3 3 0 016 0C6.5 5.5 3.5 9 3.5 9z" fill="#fff"/><circle cx="3.5" cy="3.5" r="1" fill="#262d3d"/></svg><span>42 Linden Ave - Suite 210<br>United States - GA 30310</span></div>
<div class="abs f-social" style="left:597px;top:2491px" aria-label="Social links"><i></i><i style="border-radius:50%"></i><i></i></div>

<span class="abs f-head" style="left:775px">Mailing List</span>
<p class="abs" style="left:775px;top:2378px;font-size:7px;line-height:12px;color:#fff">Enter your email address  for our mailing list<br>to keep yourself updated.</p>
<div class="abs f-input">Email address</div>
<div class="abs f-done">DONE</div>
<span class="abs" style="left:775px;top:2449px;font-size:6px;color:#9aa0ad">We Respect Your Privacy</span>
<div class="abs badge" style="left:850px;width:41px" role="img" aria-label="Made in USA badge"></div>
<div class="abs badge" style="left:901px;width:40px;border:2px solid #fff;background:#dfe3ea" role="img" aria-label="TAA compliant badge"></div>

<div class="abs footer-bar"></div>
<span class="abs bar-text" style="left:238px">© NORTHWAVE STUDIO 2018</span>
<span class="abs bar-text" style="left:736px">Home</span>
<span class="abs bar-text" style="left:769px">About</span>
<span class="abs bar-text" style="left:801px">Services</span>
<span class="abs bar-text" style="left:842px">Portfolio</span>
<span class="abs bar-text" style="left:883px">Blog</span>
<span class="abs bar-text" style="left:910px">Contact</span>

</body>
</html>
```